New Website for NY and South Florida Based Accounting Firm

Accounting and Audit firm located in New York and South Florida needs a website redesign after acquiring new businesses and adding new services.

Our current website can be found here:
http://www.tkrbwco.example/

We have merged with this firm:
http://halloranbeckwithstrand.example/

We are looking for a comprehensive design that will highlight the firm's dual locations. The final design should communicate security, strength, and growth. We would like to keep our pyramid logo as seen on the tkrbwco.example website, as this has been our logo for over 20 years.

Industry/Entity Type

Accounting

Number of Pages Required

1 page

Font styles to use
Serif
Sans Serif

```html
<!DOCTYPE html>
<html lang="en">
<head>
<meta charset="utf-8">
<title>Thornbury, Kessler, Radford &amp; Whitcombe, LLP</title>
<link href="https://fonts.googleapis.com/css2?family=Raleway:wght@400;500;600;800&family=Open+Sans:wght@400;600&display=swap" rel="stylesheet">
<style>
:root{
  --navy:#0b2466;
  --navy-deep:#06205f;
  --accent:#1c3fa8;
  --white:#ffffff;
  --band:#c3c3c3;
  --field:#ececec;
  --overlay:rgba(150,128,140,.55);
}
*{margin:0;padding:0;box-sizing:border-box}
html,body{width:1109px;height:1200px;overflow:hidden}
body{position:relative;font-family:"Open Sans",sans-serif;background:var(--white)}
.photo-backdrop{position:absolute;left:0;top:0;width:1109px;height:879px;
  background:linear-gradient(110deg,#8a8a86 0%,#b9b5ad 30%,#9c9690 50%,#6c6f78 70%,#3d4f78 100%)}
.site-header{position:absolute;left:0;top:0;width:1109px;height:76px;border-bottom:1px solid rgba(255,255,255,.35)}
.brand{position:absolute;left:43px;top:0;width:217px;height:76px;background:#f1efec;
  display:flex;align-items:center;justify-content:center;text-align:center;
  font-family:"Raleway",sans-serif;font-weight:500;font-size:15px;line-height:19px;color:var(--navy)}
.main-nav a{position:absolute;top:0;height:76px;line-height:78px;transform:translateX(-50%);
  color:var(--white);font-size:11px;text-decoration:none;white-space:nowrap}
.main-nav a.active{background:var(--navy);width:56px;text-align:center}
.hero{position:absolute;left:0;top:76px;width:1109px;height:385px;text-align:center;color:var(--white);font-family:"Raleway",sans-serif}
.hero-kicker{position:absolute;left:0;right:0;top:62px;font-weight:800;font-size:80px;letter-spacing:16px;line-height:90px}
.hero-line{position:absolute;left:0;right:0;font-weight:400;font-size:53px;line-height:60px}
.hero-line.l1{top:156px}.hero-line.l2{top:217px}
.hero-line strong{font-weight:600}
.hero-sub{position:absolute;left:0;right:0;top:286px;font-size:28px}
.hero-arrow{position:absolute;top:165px;width:38px;height:38px;border:2px solid var(--white);border-radius:50%}
.hero-arrow svg{display:block;margin:10px auto}
.services{position:absolute;left:0;top:461px;width:1109px;height:418px;background:var(--overlay);color:var(--white)}
.services h2{position:absolute;left:0;right:0;top:32px;text-align:center;font-family:"Raleway",sans-serif;font-weight:600;font-size:31px}
.service-link{position:absolute;left:225px;top:162px;width:622px;height:2px;background:var(--white)}
.service{position:absolute;top:104px;width:260px;margin-left:-130px;text-align:center}
.service .badge{width:114px;height:114px;border-radius:50%;background:var(--navy);margin:0 auto;display:flex;align-items:center;justify-content:center}
.service .badge.light{background:var(--white)}
.service h3{margin-top:20px;font-family:"Raleway",sans-serif;font-weight:600;font-size:16px;letter-spacing:1px;color:var(--accent)}
.service p{margin-top:10px;font-size:11.4px;line-height:15px}
.service .more{display:inline-block;margin-top:9px;font-size:11.4px;color:var(--white);text-decoration:none}
.service .more.blue{color:var(--accent)}
.newsletter{position:absolute;left:0;top:879px;width:1109px;height:204px;background:var(--band)}
.newsletter h2{position:absolute;left:0;right:0;top:36px;text-align:center;font-family:"Raleway",sans-serif;font-weight:600;font-size:33px;color:var(--navy)}
.field{position:absolute;top:111px;height:47px;background:var(--field);padding-left:14px;line-height:47px;font-size:11px;color:#777}
.signup{position:absolute;left:813px;top:110px;width:258px;height:48px;background:var(--navy);color:var(--white);
  text-align:center;line-height:48px;font-family:"Raleway",sans-serif;font-size:17px}
.site-footer{position:absolute;left:0;top:1083px;width:1109px;height:117px;background:var(--navy-deep);color:var(--white)}
.footer-links{position:absolute;left:394px;top:45px;font-size:11.4px;white-space:nowrap}
.footer-links span{margin:0 5px}
.copyright{position:absolute;left:446px;top:70px;font-size:9.5px}
.social{position:absolute;top:53px;width:12px;height:12px;border-radius:50%;background:#c8d0e4}
</style>
</head>
<body>
<div class="photo-backdrop" role="img" aria-label="Photograph of a businessman in a suit working at a desk with a tablet"></div>

<header class="site-header">
  <div class="brand">Thornbury, Kessler, Radford<br>&amp; Whitcombe, LLP</div>
  <nav class="main-nav">
    <a class="active" href="#" style="left:456px">HOME</a>
    <a href="#" style="left:548px">WHY TKRW?</a>
    <a href="#" style="left:643px">SERVICE</a>
    <a href="#" style="left:727px">PROFILES</a>
    <a href="#" style="left:823px">TIPS &amp; LINKS</a>
    <a href="#" style="left:931px">CLIENT LOGIN</a>
    <a href="#" style="left:1030px">CONTACT</a>
  </nav>
</header>

<section class="hero">
  <div class="hero-kicker">TKRW IS A TAX</div>
  <div class="hero-line l1">Audit and Business Advisory</div>
  <div class="hero-line l2">Practice with Over <strong>30</strong></div>
  <div class="hero-sub">Professionals in NYC and Long Island.</div>
  <div class="hero-arrow" style="left:47px"><svg width="14" height="14" viewBox="0 0 14 14"><path d="M9 2 4 7l5 5" fill="none" stroke="#fff" stroke-width="2"/></svg></div>
  <div class="hero-arrow" style="left:1029px"><svg width="14" height="14" viewBox="0 0 14 14"><path d="M5 2l5 5-5 5" fill="none" stroke="#fff" stroke-width="2"/></svg></div>
</section>

<section class="services">
  <h2>Our Service</h2>
  <div class="service-link"></div>
  <div class="service" style="left:230px">
    <div class="badge light"><svg width="50" height="46" viewBox="0 0 50 46"><path d="M14 2h32l-8 34H6z" fill="#0b2466"/><path d="M6 36h32l-1 6H5a4 4 0 0 1 1-6z" fill="none" stroke="#0b2466" stroke-width="3"/><path d="M18 12h18M16 19h18" stroke="#fff" stroke-width="3"/></svg></div>
    <h3>ACCOUNTING &amp; AUDITING</h3>
    <p>Lorem ipsum dolor sit amet, consectetur edit adipiscing elit, sed do eiusmod tempor incididunt utdolore magna aliqua.</p>
    <a class="more blue" href="#">Read More ▸</a>
  </div>
  <div class="service" style="left:558px">
    <div class="badge"><svg width="64" height="58" viewBox="0 0 64 58"><path d="M24 3h24l10 10v32H24z" fill="none" stroke="#fff" stroke-width="4"/><path d="M38 20h14M38 28h14M38 36h14" stroke="#fff" stroke-width="3"/><circle cx="25" cy="30" r="11" fill="#0b2466" stroke="#fff" stroke-width="4"/><path d="M17 38 6 52" stroke="#fff" stroke-width="6" stroke-linecap="round"/></svg></div>
    <h3>FINANCIAL PLANNING</h3>
    <p>Lorem ipsum dolor sit amet, consectetur edit adipiscing elit, sed do eiusmod tempor incididunt utdolore magna aliqua.</p>
    <a class="more" href="#">Read More ▸</a>
  </div>
  <div class="service" style="left:847px">
    <div class="badge"><svg width="54" height="54" viewBox="0 0 54 54"><rect x="3" y="8" width="48" height="43" rx="4" fill="none" stroke="#fff" stroke-width="4"/><path d="M3 18h48" stroke="#fff" stroke-width="4"/><path d="M15 2v10M39 2v10" stroke="#fff" stroke-width="5"/><text x="27" y="45" text-anchor="middle" font-family="Raleway,sans-serif" font-weight="800" font-size="22" fill="#fff">15</text></svg></div>
    <h3>TAX SERVICES</h3>
    <p>Lorem ipsum dolor sit amet, consectetur edit adipiscing elit, sed do eiusmod tempor incididunt utdolore a aliqua.</p>
    <a class="more" href="#">Read More ▸</a>
  </div>
</section>

<section class="newsletter">
  <h2>Join Our Newsletter!</h2>
  <div class="field" style="left:52px;width:358px">Enter Your Name</div>
  <div class="field" style="left:434px;width:359px">Enter Your Email id</div>
  <div class="signup">SIGN UP</div>
</section>

<footer class="site-footer">
  <div class="footer-links">Home<span>/</span>About the Company<span>/</span>Services Offered<span>/</span> Contact Us</div>
  <div class="copyright">© All Rights Reserved. Copyrights @TKRW LLP. 2016</div>
  <span class="social" style="left:902px" aria-label="Feed"></span>
  <span class="social" style="left:937px" aria-label="Social profile"></span>
  <span class="social" style="left:972px" aria-label="Social profile"></span>
  <span class="social" style="left:1007px" aria-label="Social profile"></span>
  <span class="social" style="left:1042px" aria-label="Social profile"></span>
</footer>
</body>
</html>
```